Letterhead for Law Firm Harborcrest Law Group

This would be for virtual letterhead, business cards, etc.

Also logo. I am happy to pay extra for that if it is a separate project.

Harborcrest Law Group

482 Larkmoor Avenue, Suite 730
San Francisco, California 94187

Target Market(s)

Business law services.

Industry/Entity Type

Business

Colors

Designer to choose colors to be used in the design.

```html
<!DOCTYPE html>
<html lang="en">
<head>
<meta charset="utf-8">
<title>Harborcrest Law Group — Letterhead</title>
<link href="https://fonts.googleapis.com/css2?family=Open+Sans:wght@300;400&display=swap" rel="stylesheet">
<style>
  :root {
    --brand-red: #d03522;
    --ink: #222222;
    --charcoal: #2b2b2b;
    --charcoal-light: #444444;
    --paper: #ffffff;
    --footer-text: #f2f2f2;
  }
  * { margin: 0; padding: 0; box-sizing: border-box; }
  html, body { width: 848px; height: 1200px; overflow: hidden; background: var(--paper); }
  .letterhead {
    position: relative;
    width: 848px;
    height: 1200px;
    background: var(--paper);
    font-family: "Open Sans", Arial, sans-serif;
    color: var(--ink);
    overflow: hidden;
  }
  .header-swoosh, .footer-wave { position: absolute; left: 0; display: block; }
  .header-swoosh { top: 0; }
  .footer-wave { bottom: 0; }
  .firm-name {
    position: absolute;
    top: 56px;
    right: 54px;
    display: flex;
    align-items: center;
    gap: 10px;
    font-weight: 300;
    font-size: 27px;
    letter-spacing: 0.2px;
    color: var(--ink);
    white-space: nowrap;
  }
  .firm-name .mark {
    width: 14px;
    height: 14px;
    background: var(--brand-red);
  }
  .contact-list {
    position: absolute;
    left: 28px;
    top: 1027px;
    list-style: none;
  }
  .contact-item {
    display: flex;
    align-items: center;
    gap: 12px;
    font-weight: 300;
    font-size: 19px;
    line-height: 1.2;
    white-space: nowrap;
  }
  .contact-item + .contact-item { margin-top: 18px; }
  .contact-item.address { font-size: 16px; line-height: 1.2; margin-top: 20px; }
  .contact-icon { flex: 0 0 28px; width: 28px; height: 28px; display: block; }
  .website {
    position: absolute;
    left: 462px;
    top: 1168px;
    font-weight: 300;
    font-size: 16px;
    color: var(--footer-text);
  }
</style>
</head>
<body>
<div class="letterhead">
  <svg class="header-swoosh" width="848" height="130" viewBox="0 0 848 130" aria-hidden="true">
    <path d="M0 0 H848 V4 C620 14 250 45 0 124 Z" fill="var(--charcoal)"/>
    <path d="M0 0 H848 V0 C620 8 250 34 0 112 Z" fill="var(--brand-red)"/>
  </svg>

  <div class="firm-name"><span class="mark"></span>Harborcrest Law Group</div>

  <ul class="contact-list">
    <li class="contact-item phone">
      <svg class="contact-icon" viewBox="0 0 28 28" aria-hidden="true">
        <circle cx="14" cy="14" r="14" fill="var(--brand-red)"/>
        <path d="M7.5 12 C8 9 20 9 20.5 12 L18.5 13 L17.5 11.5 H10.5 L9.5 13 Z" fill="#fff"/>
        <rect x="9" y="13.5" width="10" height="6" rx="1" fill="#fff"/>
        <circle cx="14" cy="16.5" r="1.6" fill="var(--brand-red)"/>
      </svg>
      <span>415 555 0148 (P), +1-415 555 0149 (Fax)</span>
    </li>
    <li class="contact-item email">
      <svg class="contact-icon" viewBox="0 0 28 28" aria-hidden="true">
        <circle cx="14" cy="14" r="14" fill="var(--brand-red)"/>
        <rect x="8" y="10" width="12" height="8.5" fill="#fff"/>
        <path d="M8 10 L14 15 L20 10 M8 18.5 L12.3 14 M20 18.5 L15.7 14" stroke="var(--brand-red)" stroke-width="1" fill="none"/>
      </svg>
      <span>reception@harborcrestlawgroup.com</span>
    </li>
    <li class="contact-item address">
      <svg class="contact-icon" viewBox="0 0 28 28" aria-hidden="true">
        <circle cx="14" cy="14" r="14" fill="var(--brand-red)"/>
        <path d="M6.5 14.5 L14 7.5 L21.5 14.5 L20 16 L19 15 V21 H15.8 V17 H12.2 V21 H9 V15 L8 16 Z" fill="#fff"/>
      </svg>
      <span>482 Larkmoor Avenue, Suite 730<br>San Francisco, California 94187</span>
    </li>
  </ul>

  <svg class="footer-wave" width="848" height="130" viewBox="0 1070 848 130" aria-hidden="true">
    <defs>
      <linearGradient id="footerShade" x1="0" y1="0" x2="1" y2="0">
        <stop offset="0.2" stop-color="var(--charcoal)"/>
        <stop offset="0.6" stop-color="var(--charcoal-light)"/>
        <stop offset="1" stop-color="#1e1e1e"/>
      </linearGradient>
    </defs>
    <path d="M0 1200 V1195 C300 1182 520 1150 548 1110 C555 1100 559 1092 562 1084 C620 1115 760 1168 848 1200 Z" fill="var(--brand-red)"/>
    <path d="M0 1200 C300 1192 528 1168 553 1124 C558 1115 561 1108 563 1100 C625 1136 750 1180 818 1200 Z" fill="url(#footerShade)"/>
  </svg>

  <div class="website">www.harborcrestlawgroup.com</div>
</div>
</body>
</html>
```